New lease of life for a tired Country Pub menu, QLD

I need to refresh my menus with updated prices. The menus need to be A4 (the menus are laminated and handed out over the bar. I'd like to include our logo. I will upload our existing menus as well as the new prices. The design should be humble yet stylish if that's ok, please

Target Market(s)

Locals, travellers and workers

Industry/Entity Type

Hospitality, Quintessential Country pub

Font styles to use
Sans Serif

Colors

Designer to choose colors to be used in the design.

Requirements
Must have
• as we run different menus on different nights
Nice to have
• our logo

```html
<!DOCTYPE html>
<html lang="en">
<head>
<meta charset="utf-8">
<title>Hotel Kellaway – Pizza Menu</title>
<link href="https://fonts.googleapis.com/css2?family=Anton&family=Poppins:wght@500;600;700&display=swap" rel="stylesheet">
<style>
  :root {
    --paper: #fbe9cd;
    --paper-light: #fdf0dc;
    --ink: #141414;
    --slate: #5b5b5b;
    --rule: #2a2a2a;
    --crust: #c9762f;
    --sauce: #d9482a;
    --basil: #4f8a3a;
    --onion: #c9a3c9;
  }
  * { margin: 0; padding: 0; box-sizing: border-box; }
  html, body { width: 839px; height: 1200px; overflow: hidden; background: var(--paper); }
  .menu {
    position: relative;
    width: 839px; height: 1200px;
    background: linear-gradient(165deg, var(--paper-light) 0%, var(--paper) 55%, #f9e3c2 100%);
    font-family: "Poppins", sans-serif;
    color: var(--ink);
    overflow: hidden;
  }
  .photo { position: absolute; }
  .photo--pizza-top {
    left: -24px; top: -17px; width: 250px; height: 250px; border-radius: 50%;
    background: radial-gradient(circle at 50% 50%, #e9c79a 0%, #b8683a 55%, #c98a4a 88%, #a5582a 100%);
  }
  .photo--pizza-bottom {
    left: 488px; top: 1013px; width: 416px; height: 416px; border-radius: 50%;
    background: radial-gradient(circle at 50% 50%, #f2c14a 0%, #e2582c 50%, #d8652f 80%, #c97a35 100%);
  }
  .photo--ingredients-right {
    right: 0; top: 10px; width: 100px; height: 860px;
    background: radial-gradient(ellipse at 70% 35%, rgba(217,72,42,.28), rgba(79,138,58,.12) 50%, transparent 72%);
  }
  .photo--ingredients-left {
    left: 0; top: 700px; width: 130px; height: 500px;
    background: radial-gradient(ellipse at 35% 45%, rgba(217,72,42,.28), rgba(79,138,58,.12) 50%, transparent 72%);
  }
  .photo--ingredients-bottom {
    left: 120px; top: 1110px; width: 360px; height: 90px;
    background: radial-gradient(ellipse at 50% 60%, rgba(217,72,42,.22), rgba(201,163,201,.14) 50%, transparent 72%);
  }
  .brand {
    position: absolute; left: 0; right: 0; top: 66px;
    text-align: center;
    font-family: "Poppins", sans-serif; font-weight: 700;
    font-size: 29px; line-height: 1.05; letter-spacing: .3px;
    color: var(--slate);
  }
  .title {
    position: absolute; left: 0; right: 0; top: 176px;
    text-align: center;
    font-family: "Anton", sans-serif; font-size: 108px; line-height: 1.1;
    letter-spacing: 1px; color: var(--ink);
  }
  .subtitle {
    position: absolute; left: 0; right: 0; top: 282px;
    text-align: center;
    font-weight: 700; font-size: 43px; line-height: 1.2; letter-spacing: -.5px;
    color: var(--slate);
  }
  .day-badge {
    position: absolute; left: 184px; top: 352px; width: 441px; height: 68px;
    border: 2px solid var(--ink);
    display: flex; align-items: center; justify-content: center;
    font-weight: 700; font-size: 31px; letter-spacing: .2px;
  }
  .section-heading {
    position: absolute; left: 89px; top: 440px;
    font-family: "Anton", sans-serif; font-size: 31px; line-height: 1.2;
    color: var(--slate); letter-spacing: .5px;
  }
  .items { position: absolute; left: 89px; top: 490px; width: 554px; list-style: none; }
  .item { margin-bottom: 18px; }
  .item__head { display: flex; align-items: baseline; }
  .item__name { font-weight: 600; font-size: 21px; line-height: 28px; white-space: nowrap; letter-spacing: .2px; }
  .item__leader { flex: 1; border-bottom: 1.2px solid var(--rule); margin: 0 6px 0 3px; transform: translateY(-5px); }
  .item__price { font-weight: 600; font-size: 21px; white-space: nowrap; }
  .item__price sup { font-size: 11px; vertical-align: 9px; margin-right: 1px; }
  .item__desc { font-weight: 500; font-size: 11.5px; line-height: 15.5px; max-width: 360px; margin-top: 2px; }
</style>
</head>
<body>
<main class="menu">
  <div class="photo photo--pizza-top" role="img" aria-label="Photo of a chicken and mushroom pizza seen from above"></div>
  <div class="photo photo--ingredients-right" role="img" aria-label="Scattered cherry tomatoes, basil leaves, onion rings and chillies"></div>
  <div class="photo photo--ingredients-left" role="img" aria-label="Scattered red chillies, cherry tomatoes and chilli flakes"></div>
  <div class="photo photo--ingredients-bottom" role="img" aria-label="Scattered tomatoes, basil leaf, onion ring and mushroom"></div>
  <div class="photo photo--pizza-bottom" role="img" aria-label="Photo of a pepperoni pizza with mozzarella and olives"></div>

  <div class="brand">HOTEL<br>KELLAWAY</div>

  <h1 class="title">PIZZA MENU</h1>
  <p class="subtitle">LUNCH &amp; DINNER</p>
  <div class="day-badge">WEDNESDAYS ONLY</div>

  <h2 class="section-heading">MENU ITEMS</h2>
  <ul class="items">
    <li class="item">
      <div class="item__head"><span class="item__name">HAWAIIAN</span><span class="item__leader"></span><span class="item__price"><sup>$</sup>24.50</span></div>
      <p class="item__desc">Tomato sauce, cheddar cheese, Harlow’s smoked ham and pineapple, mozzarella</p>
    </li>
    <li class="item">
      <div class="item__head"><span class="item__name">MEATLOVER’S</span><span class="item__leader"></span><span class="item__price"><sup>$</sup>25.99</span></div>
      <p class="item__desc">BBQ sauce, cheddar cheese, seasoned mince,<br>Harlow’s smoked ham, beef sausage, mozzarella</p>
    </li>
    <li class="item">
      <div class="item__head"><span class="item__name">BBQ SWEET CHILLI CHICKEN</span><span class="item__leader"></span><span class="item__price"><sup>$</sup>24.50</span></div>
      <p class="item__desc">BBQ sauce with sweet chili sauce, cheddar cheese, mushrooms, onion, chicken, mozzarella</p>
    </li>
    <li class="item">
      <div class="item__head"><span class="item__name">SUPREME</span><span class="item__leader"></span><span class="item__price"><sup>$</sup>25.99</span></div>
      <p class="item__desc">Tomato sauce, cheddar cheese, Harlow’s smoked ham, onion, capsicum, mushroom, pepperoni, pineapple, mozzarella olives</p>
    </li>
    <li class="item">
      <div class="item__head"><span class="item__name">VEGETARIAN</span><span class="item__leader"></span><span class="item__price"><sup>$</sup>24.50</span></div>
      <p class="item__desc">Tomato sauce, cheddar cheese, onion, mushroom, capsicum, olives, pumpkin</p>
    </li>
    <li class="item">
      <div class="item__head"><span class="item__name">PEPPERONI</span><span class="item__leader"></span><span class="item__price"><sup>$</sup>24.50</span></div>
      <p class="item__desc">Tomato sauce, cheddar cheese,<br>pepperoni</p>
    </li>
    <li class="item">
      <div class="item__head"><span class="item__name">TANDOORI CHICKEN</span><span class="item__leader"></span><span class="item__price"><sup>$</sup>24.50</span></div>
      <p class="item__desc">Tomato/tandoori sauce, cheddar cheese, chicken, onion, capsicum, mozzarella</p>
    </li>
  </ul>
</main>
</body>
</html>
```